Email signature

Need a dynamic email signature design thats can be compatible with desktop email, mobile, dark mode etc.
We would like to use the Kowhai Wellness logo on the left of the signature (see upload file) , with ideally icons linking our facebook page, instagram and linkedin accounts also at the bottom
Signature should include :
Name
Title
Mobile Number
Email
Addresses for Facebook https://www.socialbook.test/kowhai.wellness.nz/
Addressfor Instagram
https://www.photogram.test/kowhaiwellnessnz/
Address for Linkedin
https://www.worklink.test/company/kowhaiwellness/mycompany/

```html
<!DOCTYPE html>
<html lang="en">
<head>
<meta charset="utf-8">
<title>Kowhai Wellness – Email Signature</title>
<link rel="stylesheet" href="https://fonts.googleapis.com/css2?family=Poppins:wght@500;600;700&display=swap">
<style>
  :root {
    --backdrop: #7b7b7d;
    --cream: #f3e9e1;
    --navy: #0f2240;
    --coral: #f2714a;
    --white: #ffffff;
    --portrait-light: #e9d9cc;
    --portrait-mid: #c9b2a2;
    --portrait-ring: #f7efe9;
  }
  * { margin: 0; padding: 0; box-sizing: border-box; }
  html, body {
    width: 1200px; height: 1200px; overflow: hidden;
    background: var(--backdrop);
    font-family: "Poppins", sans-serif;
  }
  .signature {
    position: absolute; left: 75px; top: 337px;
    width: 1050px; height: 525px;
    background: var(--cream);
    box-shadow: 0 6px 18px rgba(0,0,0,0.35);
    overflow: hidden;
  }
  .brand-mark {
    position: absolute; left: 29px; top: 104px;
    width: 206px; height: 206px; border-radius: 50%;
    background: var(--navy); color: var(--white);
    display: flex; align-items: center; justify-content: center;
    text-align: center; font-weight: 600; font-size: 26px; line-height: 1.15;
  }
  .social-bar {
    position: absolute; left: 29px; top: 365px;
    width: 207px; height: 59px; border-radius: 30px;
    background: var(--coral);
    display: flex; align-items: center; justify-content: center; gap: 14px;
  }
  .social-link {
    width: 41px; height: 41px; border-radius: 50%;
    background: var(--navy); color: var(--white);
    display: flex; align-items: center; justify-content: center;
    font-weight: 600; font-size: 17px; text-decoration: none;
  }
  .divider {
    position: absolute; left: 264px; top: 49px;
    width: 3px; height: 415px; border-radius: 2px;
    background: var(--coral);
  }
  .person-name {
    position: absolute; left: 296px; top: 101px;
    font-weight: 700; font-size: 43px; color: var(--navy);
  }
  .person-title {
    position: absolute; left: 296px; top: 172px;
    font-weight: 600; font-size: 31px; color: var(--navy);
  }
  .contact-icon { position: absolute; }
  .icon-mobile { left: 306px; top: 315px; }
  .icon-email { left: 297px; top: 385px; }
  .team-photos { position: absolute; left: 580px; top: 100px; }
  .footer-band { position: absolute; left: 0; bottom: 0; }
</style>
</head>
<body>
  <div class="signature">
    <div class="brand-mark">Kowhai<br>Wellness</div>

    <nav class="social-bar">
      <a class="social-link" href="https://www.socialbook.test/kowhai.wellness.nz/" aria-label="Socialbook: kowhai.wellness.nz">S</a>
      <a class="social-link" href="https://www.photogram.test/kowhaiwellnessnz/" aria-label="Photogram: kowhaiwellnessnz">P</a>
      <a class="social-link" href="https://www.worklink.test/company/kowhaiwellness/mycompany/" aria-label="Worklink: kowhaiwellness">W</a>
    </nav>

    <div class="divider"></div>

    <h1 class="person-name">Name</h1>
    <h2 class="person-title">Title</h2>

    <svg class="contact-icon icon-mobile" width="24" height="40" viewBox="0 0 24 40" aria-label="Mobile">
      <rect x="1.5" y="1.5" width="21" height="37" rx="3" fill="none" stroke="var(--navy)" stroke-width="3"/>
      <rect x="1.5" y="1.5" width="21" height="5" fill="var(--navy)"/>
      <rect x="1.5" y="32" width="21" height="6.5" fill="var(--navy)"/>
      <circle cx="12" cy="35" r="1.4" fill="var(--cream)"/>
    </svg>

    <svg class="contact-icon icon-email" width="42" height="27" viewBox="0 0 42 27" aria-label="Email">
      <rect x="1" y="1" width="40" height="25" fill="none" stroke="var(--navy)" stroke-width="2"/>
      <path d="M1 1 L21 16 L41 1" fill="none" stroke="var(--navy)" stroke-width="2"/>
      <path d="M1 26 L16 12 M41 26 L26 12" fill="none" stroke="var(--navy)" stroke-width="2"/>
    </svg>

    <svg class="team-photos" width="470" height="340" viewBox="0 0 470 340">
      <defs>
        <radialGradient id="portrait-tone" cx="50%" cy="45%" r="60%">
          <stop offset="0%" stop-color="var(--portrait-light)"/>
          <stop offset="100%" stop-color="var(--portrait-mid)"/>
        </radialGradient>
        <radialGradient id="portrait-faint" cx="50%" cy="50%" r="50%">
          <stop offset="0%" stop-color="#e4d3c6"/>
          <stop offset="100%" stop-color="#efe3da"/>
        </radialGradient>
      </defs>
      <circle cx="128" cy="184" r="34" fill="url(#portrait-faint)" opacity="0.6" role="img" aria-label="Faded team member photo"/>
      <circle cx="457" cy="115" r="32" fill="url(#portrait-faint)" opacity="0.6" role="img" aria-label="Faded team member photo"/>
      <circle cx="213" cy="112" r="48" fill="url(#portrait-faint)" stroke="var(--portrait-ring)" stroke-width="4" opacity="0.7" role="img" aria-label="Faded team member portrait"/>
      <circle cx="480" cy="191" r="48" fill="url(#portrait-faint)" stroke="var(--portrait-ring)" stroke-width="4" opacity="0.85" role="img" aria-label="Team member portrait"/>
      <circle cx="355" cy="127" r="76" fill="url(#portrait-tone)" stroke="var(--portrait-ring)" stroke-width="5" role="img" aria-label="Team member portrait"/>
      <circle cx="235" cy="241" r="61" fill="url(#portrait-tone)" stroke="var(--portrait-ring)" stroke-width="5" role="img" aria-label="Team member portrait"/>
      <circle cx="379" cy="275" r="61" fill="url(#portrait-tone)" stroke="var(--portrait-ring)" stroke-width="5" role="img" aria-label="Team member portrait"/>
    </svg>

    <svg class="footer-band" width="1050" height="25" viewBox="0 0 1050 25">
      <path d="M0 0 H745 C758 0 765 6 772 12 L788 25 H0 Z" fill="var(--navy)"/>
    </svg>
  </div>
</body>
</html>
```